High-End Medical Center Website Design Project

This design is part of a well thought-out project by an experienced project manager / developer. The approved wireframe is attached. Creative interpretations / suggestions based on the layout encouraged.

The design is for a new state-of-the-art medical center located in Dallas, Texas. The target audience would likely be individuals (approx. 60% female /40% male) who are the healthcare decision-makers for their families. They would likely have insurance and be inclined to seek out top-quality care.

Potential clients would choose this client over others in their industry because the medical center is physician owned, meaning it is patient-focused rather than profit-focused. The facility is brand new, featuring the latest technology. (This includes an amazing waiting room featuring WiFi and docking stations.) The physicians are hand-picked by referral only.

The look of the site should be extremely clean. We are going for a well-organized, professional look with a bit of a warm glow (interpret that however you like). Use crisp corners and the colors in the logo.

Think modern, clean with some great use of color / font.

We can get lovely photography of the medical center once construction is complete. Feel free to use an "example image" behind the Featured Area ("Physician Owned. Patient-Focused") if you like. We are open to ideas.

ONE CHANGE REQUESTED IN THE WIREFRAME:

Remove the "Connect" 1/4 page footer area and replace with a quick contact form. You may swap the "Locations" area with the form if desired. Put social media icons at the top left of the page in the top header area.

(Note: Please use social media icons that match the design rather than standard icons. We preferred not placing the icons at the top, but the client requested this. Let's not bring more attention to them than necessary.)
Updates

We're custom programming this site, so there's no need to base it on a template. Also, we would prefer not to use typical "seen everywhere" stock images.Thanks.

Industry/Entity Type

Construction

Requirements
Must have
• Follow the wireframe. This has been approved.
Nice to have
• Examples of what hover states, links or dropdowns might look like.

```html
<!DOCTYPE html>
<html lang="en">
<head>
<meta charset="utf-8">
<title>Lumen Medical Center</title>
<link rel="stylesheet" href="https://fonts.googleapis.com/css2?family=Open+Sans:wght@300;400;600&family=PT+Sans:wght@400;700&display=swap">
<style>
:root{
  --blue:#0a4c9c;
  --teal:#3a9ca9;
  --teal-dark:#2f8492;
  --ink:#333;
  --muted:#555;
  --grey-text:#8c8c8c;
  --page:#f0f0f0;
  --topbar:#232323;
  --footer:#2b2b2b;
  --white:#fff;
}
*{box-sizing:border-box;margin:0;padding:0}
html,body{width:962px;height:1200px;overflow:hidden}
body{position:relative;background:var(--page);font-family:"Open Sans",Arial,sans-serif;color:var(--ink)}
.abs{position:absolute}
.topbar{left:0;top:0;width:962px;height:14px;background:var(--topbar);color:#eee;font-size:9px;line-height:14px;text-align:right;padding-right:93px}
.header{left:0;top:14px;width:962px;height:89px;background:linear-gradient(#f6f6f6,#fff 40%);border-bottom:2px solid #d8d8d8}
.brand{left:89px;top:24px;display:flex;align-items:center;gap:7px;font-family:"PT Sans",sans-serif;font-weight:700;font-size:19px;color:var(--blue);letter-spacing:.5px}
.brand-mark{width:14px;height:14px;background:var(--teal)}
.nav{right:93px;top:26px;display:flex;align-items:center;gap:2px;font-size:10.5px}
.nav a{color:#111;text-decoration:none;padding:6px 6px;border-radius:5px}
.nav a.active{background:var(--blue);color:#fff;padding:6px 8px}
.hero{left:0;top:104px;width:962px;height:380px;background:radial-gradient(ellipse at 50% 55%,#4f9aa6 0%,#2f7a8a 45%,#1c5566 100%)}
.hero-shadow{left:40px;top:480px;width:882px;height:14px;background:radial-gradient(ellipse at 50% 0,rgba(0,0,0,.45),rgba(0,0,0,0) 70%)}
.hero-title{left:0;top:200px;width:962px;text-align:center;color:#fff;font-family:"PT Sans",sans-serif;font-size:60px;letter-spacing:-2.5px;text-shadow:0 2px 4px rgba(0,0,0,.35)}
.hero-link{top:285px;width:100px;text-align:center;color:#fff;font-family:"PT Sans",sans-serif;font-size:16px}
.hero-link .ring{width:78px;height:78px;margin:0 auto 4px;border:3.5px solid #fff;border-radius:50%;display:flex;align-items:center;justify-content:center}
.card{top:539px;width:210px;height:170px;background:#fff;box-shadow:0 1px 3px rgba(0,0,0,.25)}
.card-head{height:42px;background:var(--blue);color:#fff;display:flex;align-items:center;gap:8px;padding-left:13px;font-family:"PT Sans",sans-serif;font-size:17.5px}
.card-body{padding:12px 12px 0;font-size:10.3px;line-height:13.6px;color:var(--muted)}
.card .more{position:absolute;right:10px;bottom:4px;font-size:9px;color:var(--teal);text-decoration:underline}
.divider{left:130px;top:749px;width:680px;height:1px;background:linear-gradient(90deg,transparent,#d2d2d2,transparent)}
.portrait{left:99px;top:787px;width:132px;height:127px;background:#fff;padding:4px;box-shadow:0 0 2px rgba(0,0,0,.1)}
.portrait div{width:100%;height:100%;background:linear-gradient(135deg,#c9c4bc,#8e9aa6 60%,#34465e)}
h2{font-family:"PT Sans",sans-serif;font-weight:400;color:#222}
.welcome{left:240px;top:786px;width:300px}
.welcome h2{font-size:21px;margin-bottom:8px}
.welcome p{font-size:10.8px;line-height:15.2px;color:#444;margin-bottom:15px}
.testimonials{left:649px;top:785px;width:216px}
.testimonials h2{font-size:19px;margin-bottom:5px}
.quote{position:relative;background:var(--teal);color:#fff;font-family:"PT Sans",sans-serif;font-size:10.2px;line-height:14.4px;padding:8px 5px 8px 10px;box-shadow:0 1px 2px rgba(0,0,0,.2)}
.quote-tail{position:absolute;right:20px;bottom:-25px}
.author{left:690px;top:899px;width:88px;text-align:right;font-family:"PT Sans",sans-serif}
.author b{display:block;font-size:9.5px;color:#333}
.author span{font-size:8.5px;color:#666}
.avatar{left:784px;top:896px;width:27px;height:31px;background:linear-gradient(#c8c8c8,#9c9c9c)}
.pager{left:787px;top:936px;width:76px;height:13px;border:1px solid #ddd;border-radius:7px;background:#fff;display:flex;align-items:center;gap:3px;padding-left:4px;font-size:6.5px;color:#777}
.pager i{width:6px;height:6px;border-radius:50%;background:#c4c4c4;display:block}
.pager i.on{background:#555}
.lower{left:0;top:956px;width:962px;height:198px;background:#fff;border-top:1px solid #e2e2e2}
.col h3{font-family:"PT Sans",sans-serif;font-weight:400;font-size:13px;color:#222;margin-bottom:10px}
.post p{font-size:9.5px;line-height:12px;color:#555}
.post time{display:block;font-size:9.5px;color:#222;margin:4px 0 30px}
.field{display:block;width:160px;height:18px;border:1px solid #cfcfcf;box-shadow:inset 0 1px 2px rgba(0,0,0,.08);font-size:7px;color:#444;padding:4px 7px;margin-bottom:7px;background:#fff}
.field.tall{height:32px}
.submit{width:65px;height:19px;background:var(--teal);color:#fff;font-family:"PT Sans",sans-serif;font-weight:700;font-size:9.5px;border-radius:2px;text-align:center;line-height:19px;margin-top:3px}
.wait-value{color:var(--teal);font-size:11.5px;margin:-6px 0 4px -2px}
.wait-text{font-size:9.5px;line-height:14.4px;color:var(--grey-text);margin-left:-2px}
.footer{left:0;top:1154px;width:962px;height:46px;background:var(--footer);color:#aaa;font-size:8.8px;line-height:46px}
.footer .copy{left:110px}
.footer .legal{right:114px}
</style>
</head>
<body>
<div class="abs topbar">Call Now: (555) 014-2290</div>

<header class="abs header"></header>
<div class="abs brand"><span class="brand-mark"></span>LUMEN MEDICAL CENTER</div>
<nav class="abs nav">
  <a class="active" href="#">Why Lumen</a><a href="#">Physician</a><a href="#">Specialities</a><a href="#">Info</a><a href="#">Locations</a><a href="#">Contact</a>
</nav>

<section class="abs hero" role="img" aria-label="Photo of a hospital corridor with staff walking beside a bed"></section>
<div class="abs hero-shadow"></div>
<h1 class="abs hero-title" style="font-weight:400">Physician Owned Patient Focused</h1>

<div class="abs hero-link" style="left:285px">
  <div class="ring"><svg width="44" height="44" viewBox="0 0 44 44" fill="none" stroke="#fff" stroke-width="3" stroke-linecap="round"><path d="M10 6v10a8 8 0 0 0 16 0V6"/><path d="M18 24v6a7 7 0 0 0 14 0v-3"/><circle cx="32" cy="23" r="4"/></svg></div>Medical
</div>
<div class="abs hero-link" style="left:408px">
  <div class="ring"><svg width="44" height="44" viewBox="0 0 44 44" fill="#fff"><path d="M6 18 22 6l16 12v18H6z"/><path d="M6 18l16 12 16-12" fill="none" stroke="#2f7a8a" stroke-width="2"/><rect x="14" y="12" width="16" height="12" fill="#fff" stroke="#2f7a8a" stroke-width="1.5"/></svg></div>Email
</div>
<div class="abs hero-link" style="left:530px">
  <div class="ring"><svg width="44" height="44" viewBox="0 0 44 44"><path d="M22 6a15 14 0 1 1-8 26l-7 4 3-8A15 14 0 0 1 22 6z" fill="#fff"/><text x="22" y="28" text-anchor="middle" font-family="Arial,sans-serif" font-weight="700" font-size="18" fill="#2f7a8a">?</text></svg></div>Why Lumen
</div>

<article class="abs card" style="left:103px">
  <div class="card-head"><svg width="17" height="17" viewBox="0 0 20 20"><circle cx="10" cy="10" r="6" fill="none" stroke="#fff" stroke-width="4" stroke-dasharray="3 1.7"/><circle cx="10" cy="10" r="5" fill="#fff"/><circle cx="10" cy="10" r="2.2" fill="#0a4c9c"/></svg>Technology</div>
  <p class="card-body">Lorem Ipsum is simply dummy text of the printing and typesetting industry. Lorem Ipsum has been the industry's standard dummy text ever since the 1500s, when an unknown printer took a galley of type and scrambled it to make a type specimen book.</p>
  <a class="more">Read More</a>
</article>
<article class="abs card" style="left:382px">
  <div class="card-head"><svg width="18" height="18" viewBox="0 0 20 20"><circle cx="10" cy="10" r="9" fill="#fff"/><path d="M10 5v10M5 10h10" stroke="#0a4c9c" stroke-width="3"/></svg>Quality Of Care</div>
  <p class="card-body">Lorem Ipsum is simply dummy text of the printing and typesetting industry. Lorem Ipsum has been the industry's standard dummy text ever since the 1500s, when an unknown printer took a galley of type and scrambled it to make a type specimen book.</p>
  <a class="more">Read More</a>
</article>
<article class="abs card" style="left:662px">
  <div class="card-head"><svg width="16" height="18" viewBox="0 0 16 18" fill="#fff"><circle cx="8" cy="4.5" r="3.5"/><path d="M1 18v-5a5 5 0 0 1 5-5h4a5 5 0 0 1 5 5v5z"/></svg>Patient Experience</div>
  <p class="card-body">Lorem Ipsum is simply dummy text of the printing and typesetting industry. Lorem Ipsum has been the industry's standard dummy text ever since the 1500s, when an unknown printer took a galley of type and scrambled it to make a type specimen book.</p>
  <a class="more">Read More</a>
</article>

<div class="abs divider"></div>

<figure class="abs portrait"><div role="img" aria-label="Photo of a doctor talking with an older patient"></div></figure>
<section class="abs welcome">
  <h2>Welcome to Lumen Medical</h2>
  <p>This site was created for patients and all people who want information about safe Aesthetic and Reconstructive Plastic Surgery and health in general.</p>
  <p>Undoubtedly, well-informed patients have greater confidence and decision-making ability.</p>
</section>

<section class="abs testimonials">
  <h2>Testimonials</h2>
  <blockquote class="quote">Integer vehicula velit quis ante ornare iaculis. Sed sed neque metus. Nullam mauris metus, bibendum at facilisis nec, ullamcorper sit amet orci. Nulla facilisi.
    <svg class="quote-tail" width="26" height="26" viewBox="0 0 26 26"><path d="M0 0h26L0 26z" fill="#3a9ca9"/></svg>
  </blockquote>
</section>
<div class="abs author"><b>Daniel Whitmore</b><span>CEO, Lumen Medical</span></div>
<div class="abs avatar" role="img" aria-label="Profile picture placeholder"></div>
<div class="abs pager"><i></i><i class="on"></i><i></i><i></i><i></i><span>NEXT</span></div>

<section class="abs lower"></section>
<div class="abs col" style="left:108px;top:980px;width:200px">
  <h3>Recent Posts</h3>
  <div class="post"><p>Lorem Ipsum is simply dummy text of the printing and typesetting industry.</p><time>June 30, 2013</time></div>
  <div class="post"><p>Lorem Ipsum is simply dummy text of the printing and typesetting industry.</p><time>June 25, 2013</time></div>
</div>
<div class="abs col" style="left:397px;top:980px;width:170px">
  <h3>Newsletter</h3>
  <span class="field">Enter your name...</span>
  <span class="field">Enter your email</span>
  <span class="field tall">Enter your message</span>
  <div class="submit">SUBMIT</div>
</div>
<div class="abs col" style="left:662px;top:980px;width:200px">
  <h3>Average wait time</h3>
  <p class="wait-value">9 Minutes</p>
  <p class="wait-text">Lorem ipsum dolor sit amet, consectetuer adipiscing elit, sed diam nonummy nibh euismod tincidunt ut laoreet dolore magna aliquam erat volutpat ed diam nonummy nibh euismod tincidunt ut.</p>
</div>

<footer class="abs footer">
  <span class="abs copy">Copyright © Lumen Medical. All rights reserved.</span>
  <span class="abs legal">Privacy Policy &nbsp;|&nbsp; Terms &amp; Conditions</span>
</footer>
</body>
</html>
```